Landing page for new software as a service product

==== ENGLISH VERSION ====

Due to our excellent customer service, the company FernHaven has gained many satisfied customers. Now we have developed a new product, which enables companies in times of Covid-19 to use a video salesroom, to get in contact with their customers. In contrast to many other solutions on the market, it is not only an outbound solution. Our solution can handle incoming calls from the website / shop / app of a customer. The video call is routed by different rules (regarding day of week, time and sales agent) to the correct sales agent. If no sales agent is available different exit strategies are available to not loose the lead.

We need a LANDING PAGE for this application (no backend design!), Which can later be translated into different languages. Attached are screenshots of the application, which can be used if required. If you need other information, you are free to contact us and we try to provide these information to you.

==== GERMAN VERSION ====

As a cloud provider, FernHaven has gained many satisfied customers through excellent customer service in recent years. Now we have developed a new product that enables companies to make sales via video. And not just in the outbound, as known from well-known providers, but also in the inbound. This means that the customer can start a video call to the dealer using a button on the homepage. The call is then routed to the appropriate employee as with a correct telephone system according to previously defined rules (date, time, user groups).

For this application we need a landing page, which can later be translated into other languages. Screenshots of the application are included and additional ones can be created if required. As a technician, it is difficult for us to select the correct information here. So if there is a need for more information, we can certainly provide it if it is named.
Updates

I've made the mistake and made only a german briefing, which was really not suitable for the most designers. I've fixed this error and translated the briefing now.

Requirements
Must have
• A landing page design, for the new product. Please only designs which fits the topic and not some generic designs which need to be customized by us ... If we we're able to do this, we would not ask for help here ;-)
Should not have
• We do not need an admin template for the application, we already have an admin design.

```html
<!DOCTYPE html>
<html lang="en">
<head>
<meta charset="utf-8">
<title>FernHaven – Video Salesroom</title>
<link href="https://fonts.googleapis.com/css2?family=Poppins:wght@400;500;600&family=Lato:wght@400;700&display=swap" rel="stylesheet">
<style>
:root{
  --navy:#0b1d5a;
  --navy-deep:#081647;
  --ink:#132c7c;
  --text:#4a4f5c;
  --red:#d5161c;
  --soft:#eaf1fa;
  --blob:#e2eef9;
  --app-blue:#0a55ff;
  --app-green:#7aa41a;
  --step-blue:#4bb7dd;
  --step-green:#5fb85a;
  --line:#d6d9de;
}
*{box-sizing:border-box;margin:0;padding:0}
html,body{width:1200px;height:3125px;overflow:hidden}
body{position:relative;background:#fff;font-family:'Lato',sans-serif;color:var(--text)}
.abs{position:absolute}
h1,h2,h3{font-family:'Poppins',sans-serif;font-weight:400;color:var(--ink)}

/* hero */
.hero{left:0;top:0;width:1200px;height:522px;background:radial-gradient(ellipse at 80% 85%,#1b6a9a 0%,#123f7e 25%,var(--navy) 60%,var(--navy-deep) 100%)}
.brand{left:215px;top:22px;font-family:'Poppins',sans-serif;font-size:20px;font-weight:500;color:#fff}
.nav{top:29px;font-family:'Poppins',sans-serif;font-size:10.5px;color:#fff}
.btn-red{background:var(--red);color:#fff;font-family:'Poppins',sans-serif;font-weight:600;font-size:9.5px;letter-spacing:.3px;border-radius:14px;display:flex;align-items:center;justify-content:center}
.hero-sub{left:0;width:1200px;top:122px;text-align:center;color:#fff;font-size:11px}
.hero-title{left:0;width:1200px;top:148px;text-align:center;color:#fff;font-size:32px;line-height:36px;font-weight:400}

/* laptop */
.laptop{left:359px;top:262px;width:461px;height:305px;background:#f3f4f6;border-radius:14px 14px 0 0;box-shadow:0 10px 30px rgba(0,0,0,.08)}
.screen{left:18px;top:16px;width:425px;height:262px;background:#fff;border-bottom:6px solid #333}
.laptop-base{left:307px;top:570px;width:563px;height:12px;background:linear-gradient(#f4f5f7,#dfe1e5);border-radius:0 0 40px 40px;box-shadow:0 20px 30px rgba(0,0,0,.08)}
.tabs{left:0;top:0;width:425px;height:10px;border-bottom:1px solid #eee;font-size:3.5px;color:#666;display:flex;gap:10px;padding:3px 0 0 2px}
.tabs b{color:var(--app-green);font-weight:700}
.dash-title{left:4px;top:17px;font-size:9px;color:var(--app-green)}
.card{top:38px;width:150px;height:77px;background:#f7f7f8;border:1px solid #e8e8e8}
.card small{position:absolute;bottom:2px;left:0;width:100%;text-align:center;font-size:3.5px;color:#777}
.chart{top:122px;height:124px;background:#fbfbfb;border:1px solid #ececec}
.chart svg{position:absolute;left:0;top:0}

/* about */
.h2{font-size:25px}
.para{font-size:9.5px;line-height:15px;color:var(--text)}
.btn-line{left:237px;top:842px;width:109px;height:27px;border:2px solid var(--ink);border-radius:14px;color:var(--ink);font-family:'Poppins',sans-serif;font-weight:600;font-size:9px;letter-spacing:.6px;display:flex;align-items:center;justify-content:center}
.art{background:linear-gradient(135deg,#e5eefb,#f0d9bd 55%,#dfe9f8)}

/* why */
.why{left:0;top:965px;width:1200px;height:472px;background:var(--soft)}
.feature{width:200px;text-align:center}
.feature .ico{width:64px;height:60px;margin:0 auto;background:linear-gradient(160deg,#c9d6ee,#a9bde3);border-radius:50%}
.feature h3{font-size:11px;font-weight:600;color:#1d47a8;margin-top:10px}
.feature p{font-size:9.5px;line-height:14px;margin-top:2px;color:#6b7080}

/* app window */
.blob{background:var(--blob);border-radius:48% 52% 46% 54%/55% 50% 50% 45%}
.win{width:453px;height:308px;background:#fff;box-shadow:0 6px 24px rgba(20,40,90,.18);overflow:hidden;font-family:Arial,sans-serif}
.win .bar{position:absolute;left:0;top:0;width:100%;height:11px;background:#e4e4e4}
.win .side{position:absolute;left:0;top:11px;width:36px;height:297px;background:var(--app-blue)}
.win .ttl{position:absolute;left:40px;top:20px;font-size:8.5px;font-weight:700;color:var(--app-green)}
.win .x{position:absolute;right:6px;top:19px;font-size:9px;color:#333}
.win .top-line{position:absolute;left:36px;top:36px;width:417px;border-top:1px solid #eee}
.steps{position:absolute;left:40px;top:55px;width:405px;height:27px;display:flex}
.step{flex:1;font-size:6.5px;color:#999;text-align:center;padding-top:5px;background:#f1f1f1;clip-path:polygon(0 0,93% 0,100% 50%,93% 100%,0 100%,6% 50%)}
.step:first-child{clip-path:polygon(0 0,93% 0,100% 50%,93% 100%,0 100%)}
.step span{display:block;font-size:5px;margin-top:2px}
.step.on{color:#fff}
.step.b{background:var(--step-blue)}
.step.g{background:var(--step-green)}
.win .txt{position:absolute;left:66px;width:360px;font-size:7px;line-height:11px;color:#222}
.lbl{position:absolute;font-size:7px;color:#222}
.inp{position:absolute;height:18px;border:1px solid #cfd3d8;border-radius:2px;font-size:8px;color:#555;padding:4px 5px}
.inp .clk{position:absolute;right:0;top:0;width:20px;height:16px;border-left:1px solid #cfd3d8;background:#f3f3f3}
.btn-app{position:absolute;top:0;height:16px;font-size:7px;color:#fff;display:flex;align-items:center;justify-content:center;border-radius:2px}

/* cta */
.cta{left:0;top:2928px;width:1200px;height:140px;background:#0c2475}
.footer{left:0;top:3092px;width:1200px;text-align:center;font-size:9px;color:#444}
.footer u{color:#1b3a94}
</style>
</head>
<body>

<!-- HERO -->
<section class="abs hero" role="img" aria-label="Dark blue background with glowing particle waves and light streaks"></section>
<div class="abs brand">FernHaven</div>
<nav>
  <span class="abs nav" style="left:510px">Who we are</span>
  <span class="abs nav" style="left:582px">What We Offer</span>
  <span class="abs nav" style="left:668px">Features</span>
  <span class="abs nav" style="left:727px">Contact Us</span>
  <a class="abs btn-red" style="left:801px;top:22px;width:132px;height:28px">REQUEST A DEMO</a>
  <span class="abs nav" style="left:951px">EN
    <svg width="8" height="6" viewBox="0 0 8 6"><path d="M1 1l3 3 3-3" stroke="#fff" fill="none"/></svg></span>
</nav>
<p class="abs hero-sub">Our solution can handle incoming calls from the website / shop / app of a customer</p>
<h1 class="abs hero-title">Connect with your customers<br>easily in times of Covid-19</h1>

<div class="abs laptop">
  <div class="abs screen">
    <div class="abs tabs"><b>VIDEO SALES ROOM</b><b>DASHBOARD</b><span>SESSIONS</span><span>USERS</span><span>CALL GROUPS</span><span>CALLFLOW</span><span>CALL HISTORY</span></div>
    <div class="abs dash-title">DASHBOARD</div>
    <div class="abs card" style="left:8px">
      <svg class="abs" style="left:64px;top:20px" width="20" height="30" viewBox="0 0 20 30"><rect x="3" y="1" width="14" height="28" rx="2" fill="none" stroke="#8cb21f" stroke-width="2"/><rect x="6" y="9" width="8" height="7" fill="none" stroke="#8cb21f" stroke-width="1.5"/></svg>
      <small>Active Video Call</small></div>
    <div class="abs card" style="left:164px">
      <svg class="abs" style="left:55px;top:18px" width="40" height="36" viewBox="0 0 40 36"><path d="M6 30A16 16 0 1 1 34 30" fill="none" stroke="#bbb" stroke-width="6"/><path d="M6 30A16 16 0 0 1 10 10" fill="none" stroke="#555" stroke-width="6"/></svg>
      <small>Agents online now</small></div>
    <div class="abs card" style="left:320px;width:105px">
      <span class="abs" style="left:66px;top:20px;font-size:24px;color:#222">0</span>
      <small>Incoming calls today</small></div>
    <div class="abs chart" style="left:8px;width:306px">
      <svg width="306" height="124"><g stroke="#e6e6e6"><path d="M20 15H300M20 35H300M20 55H300M20 75H300M20 95H300"/></g><path d="M20 10V100H300" stroke="#999" fill="none"/></svg>
      <small class="abs" style="left:0;bottom:3px;width:100%;text-align:center;font-size:3.5px;color:#777">Today calls</small></div>
    <div class="abs chart" style="left:320px;width:105px">
      <svg width="105" height="124"><g stroke="#e6e6e6"><path d="M20 15H100M20 35H100M20 55H100M20 75H100M20 95H100"/></g><path d="M20 10V100H100" stroke="#999" fill="none"/></svg></div>
  </div>
</div>
<div class="abs laptop-base"></div>

<!-- ABOUT -->
<h2 class="abs h2" style="left:237px;top:666px">A few words about us</h2>
<p class="abs para" style="left:237px;top:716px;width:295px">Lorem ipsum dolor sit amet, consectetur adipiscing elit, sed do eiusmod tempor incididunt ut labore et dolore magna aliqua. Quis ipsum suspendisse ultrices gravida. Risus commodo viverra maecenas accumsan lacus vel facilisis. Lorem ipsum dolor sit amet, consectetur adipiscing elit, sed do eiusmod tempor incididunt ut labore et dolore magna aliqua. Quis ipsum suspendisse ultrices gravida. Risus commodo viverra maecenas accumsan lacus vel facilisis.</p>
<a class="abs btn-line">KNOW MORE</a>
<div class="abs art blob" style="left:565px;top:661px;width:424px;height:213px" role="img" aria-label="Illustration of two people working beside a large monitor showing a secure dashboard"></div>

<!-- WHY -->
<section class="abs why"></section>
<h2 class="abs h2" style="left:0;width:1200px;text-align:center;top:1024px">Why choose us</h2>
<p class="abs para" style="left:360px;width:480px;top:1068px;text-align:center;color:#777">Lorem ipsum dolor sit amet, consectetur adipiscing elit, sed do eiusmod tempor incididunt ut labore et dolore magna aliqua. Quis ipsum suspendisse ultrices gravida. Risus commodo viverra maecenas accumsan lacus vel facilisis.</p>

<div class="abs feature" style="left:238px;top:1128px"><div class="ico" role="img" aria-label="Stopwatch icon"></div><h3>Quick Results</h3><p>Lorem ipsum dolor sit amet, consectetur adipiscing elit.</p></div>
<div class="abs feature" style="left:508px;top:1128px"><div class="ico" role="img" aria-label="Monitor with gears icon"></div><h3>Powerful Interface</h3><p>Lorem ipsum dolor sit amet, consectetur adipiscing elit.</p></div>
<div class="abs feature" style="left:761px;top:1128px"><div class="ico" role="img" aria-label="Piggy bank icon"></div><h3>Money Saving</h3><p>Lorem ipsum dolor sit amet, consectetur adipiscing elit.</p></div>
<div class="abs feature" style="left:238px;top:1263px"><div class="ico" role="img" aria-label="Support agent with headset icon"></div><h3>Efficient Support</h3><p>Lorem ipsum dolor sit amet, consectetur adipiscing elit.</p></div>
<div class="abs feature" style="left:508px;top:1263px"><div class="ico" role="img" aria-label="Light bulb with gears icon"></div><h3>Innovative Technologies</h3><p>Lorem ipsum dolor sit amet, consectetur adipiscing elit.</p></div>
<div class="abs feature" style="left:761px;top:1263px"><div class="ico" role="img" aria-label="Code window icon"></div><h3>Great Usability</h3><p>Lorem ipsum dolor sit amet, consectetur adipiscing elit.</p></div>

<!-- FLOW STEP 1 -->
<div class="abs blob" style="left:185px;top:1517px;width:400px;height:405px"></div>
<div class="abs win" style="left:155px;top:1571px">
  <div class="bar"></div><div class="side"></div>
  <div class="ttl">CREATE NEW CALL FLOW</div><div class="x">✕</div><div class="top-line"></div>
  <div class="steps" style="top:58px">
    <div class="step on b">Basic informations<span>Times and Description</span></div>
    <div class="step">Call Routing<span>Who should receive calls</span></div>
    <div class="step">Escalation<span>Where to send the user</span></div>
  </div>
  <p class="txt" style="top:115px">To provide a better customer journey you can create multiple call flows. Every call flow will route an incoming video call according to its specifications. In this first step, please provide a short name to identify this callflow and times when this callflow should be active.</p>
  <span class="lbl" style="left:67px;top:155px">Name</span><span class="lbl" style="left:246px;top:155px">Description</span>
  <div class="inp" style="left:67px;top:171px;width:174px">Name</div>
  <div class="inp" style="left:246px;top:171px;width:174px">Description</div>
  <span class="lbl" style="left:73px;top:208px;font-weight:700">Day of Week</span>
  <span class="lbl" style="left:130px;top:208px;font-weight:700">Start Time</span>
  <span class="lbl" style="left:278px;top:208px;font-weight:700">End Time</span>
  <div class="abs" style="left:67px;top:221px;width:353px;border-top:1px solid #ccc"></div>
  <span class="lbl" style="left:73px;top:236px">Monday</span>
  <div class="inp" style="left:129px;top:230px;width:136px">00:00<i class="clk"></i></div>
  <div class="inp" style="left:277px;top:230px;width:136px">00:00<i class="clk"></i></div>
  <span class="lbl" style="left:73px;top:267px">Tuesday</span>
  <div class="inp" style="left:129px;top:261px;width:136px">00:00<i class="clk"></i></div>
  <div class="inp" style="left:277px;top:261px;width:136px">00:00<i class="clk"></i></div>
  <span class="lbl" style="left:73px;top:298px">Wednesday</span>
  <div class="inp" style="left:129px;top:292px;width:136px">00:00<i class="clk"></i></div>
  <div class="inp" style="left:277px;top:292px;width:136px">00:00<i class="clk"></i></div>
</div>
<h2 class="abs h2" style="left:688px;top:1643px;line-height:30px">Lorem ipsum dolor<br>sit amet</h2>
<p class="abs para" style="left:688px;top:1718px;width:260px">Lorem ipsum dolor sit amet, consectetur adipiscing elit, sed do eiusmod tempor incididunt ut labore et dolore magna aliqua. Quis ipsum suspendisse ultrices gravida. Risus commodo viverra maecenas accumsan lacus vel facilisis. Lorem ipsum dolor sit amet, consectetur adipiscing elit, sed do eiusmod tempor incididunt ut labore et dolore magna aliqua.</p>

<!-- FLOW STEP 2 -->
<div class="abs blob" style="left:598px;top:1960px;width:400px;height:405px"></div>
<div class="abs win" style="left:567px;top:2014px">
  <div class="bar"></div><div class="side"></div>
  <div class="ttl" style="left:44px">CREATE NEW CALL FLOW</div><div class="x">✕</div><div class="top-line"></div>
  <div class="steps" style="left:44px;top:56px">
    <div class="step on g">Basic informations<span>Times and Description</span></div>
    <div class="step on b">Call Routing<span>Who should receive calls</span></div>
    <div class="step">Escalation<span>Where to send the user</span></div>
  </div>
  <p class="txt" style="left:72px;top:114px;width:345px">In this second step, you need to select which callgroup will receive a call and how long this call will ring in this callgroup, before the system selects the next callgroup. Please be aware that the total time should not be too long, or the user will cancel the call.</p>
  <div class="abs" style="left:72px;top:160px;width:345px;height:98px;border:1px solid #e2e2e2"></div>
  <span class="lbl" style="left:78px;top:166px;font-weight:700">Ringtime (seconds)</span>
  <span class="lbl" style="left:163px;top:166px;font-weight:700">Callgroup</span>
  <span class="lbl" style="left:337px;top:166px;font-weight:700">Action</span>
  <div class="abs" style="left:72px;top:178px;width:345px;border-top:1px solid #ddd"></div>
  <div class="inp" style="left:78px;top:184px;width:76px">15</div>
  <div class="inp" style="left:163px;top:184px;width:163px;font-size:7px">Test0 (Product 1 Sales Rep)</div>
  <div class="inp" style="left:78px;top:215px;width:76px">30</div>
  <div class="inp" style="left:163px;top:215px;width:163px;font-size:7px">Test3 (Product 2 Sales Rep)</div>
  <svg class="abs" style="left:337px;top:188px" width="24" height="40"><rect x="0" y="2" width="7" height="8" fill="#8bbd2a"/><rect x="10" y="1" width="9" height="9" fill="#5fa532"/><rect x="0" y="32" width="7" height="8" fill="#8bbd2a" transform="translate(0,-3)"/><rect x="10" y="28" width="9" height="9" fill="#5fa532"/></svg>
  <div class="abs" style="left:336px;top:250px;width:110px;height:16px">
    <div class="btn-app" style="left:0;width:40px;background:#1796b8">Previous</div>
    <div class="btn-app" style="left:44px;width:26px;background:#1796b8">Next</div>
    <div class="btn-app" style="left:74px;width:28px;background:#8fd0e4">Save</div>
  </div>
</div>
<h2 class="abs h2" style="left:234px;top:2098px;line-height:30px">Lorem ipsum dolor<br>sit amet</h2>
<p class="abs para" style="left:234px;top:2173px;width:260px">Lorem ipsum dolor sit amet, consectetur adipiscing elit, sed do eiusmod tempor incididunt ut labore et dolore magna aliqua. Quis ipsum suspendisse ultrices gravida. Risus commodo viverra maecenas accumsan lacus vel facilisis. Lorem ipsum dolor sit amet, consectetur adipiscing elit, sed do eiusmod tempor incididunt ut labore et dolore magna aliqua.</p>

<!-- FLOW STEP 3 -->
<div class="abs blob" style="left:185px;top:2443px;width:400px;height:405px"></div>
<div class="abs win" style="left:155px;top:2497px">
  <div class="bar"></div><div class="side"></div>
  <div class="ttl" style="left:42px">CREATE NEW CALL FLOW</div><div class="x">✕</div><div class="top-line"></div>
  <div class="steps" style="left:42px;top:57px">
    <div class="step on g">Basic informations<span>Times and Description</span></div>
    <div class="step on g">Call Routing<span>Who should receive calls</span></div>
    <div class="step on b">Escalation<span>Where to send the user</span></div>
  </div>
  <p class="txt" style="left:70px;top:115px;width:350px">If on your side nobody is available for a call or the call is made outside the available hours, the user should be routed to a place where he can leave a message or this lead might be lost. Please specify in this step the url, where the user should be redirected to if nobody answers his call.</p>
  <span class="lbl" style="left:70px;top:160px">Exit URL</span>
  <div class="inp" style="left:70px;top:172px;width:349px">URL</div>
  <span class="lbl" style="left:70px;top:201px">Out of business hours URL</span>
  <div class="inp" style="left:70px;top:213px;width:349px">URL</div>
  <span class="lbl" style="left:70px;top:242px">Escalation URL</span>
  <div class="inp" style="left:70px;top:255px;width:349px">URL</div>
</div>
<h2 class="abs h2" style="left:688px;top:2570px;line-height:30px">Lorem ipsum dolor<br>sit amet</h2>
<p class="abs para" style="left:688px;top:2645px;width:260px">Lorem ipsum dolor sit amet, consectetur adipiscing elit, sed do eiusmod tempor incididunt ut labore et dolore magna aliqua. Quis ipsum suspendisse ultrices gravida. Risus commodo viverra maecenas accumsan lacus vel facilisis. Lorem ipsum dolor sit amet, consectetur adipiscing elit, sed do eiusmod tempor incididunt ut labore et dolore magna aliqua.</p>

<!-- CTA -->
<section class="abs cta"></section>
<h2 class="abs h2" style="left:233px;top:2958px;color:#fff">Request your demo today!</h2>
<p class="abs para" style="left:233px;top:3003px;width:520px;color:#fff">Lorem ipsum dolor sit amet, consectetur adipiscing elit, sed do eiusmod tempor incididunt ut labore et dolore magna aliqua. Quis ipsum suspendisse ultrices gravida.</p>
<a class="abs btn-red" style="left:832px;top:2988px;width:119px;height:27px">CONTACT US</a>

<footer class="abs footer">© 2020 Copyright FernHaven. All Rights Reserved. <u>Privacy Policy</u> | <u>Terms &amp; Conditions</u></footer>

</body>
</html>
```